Brixel Solutions Website Creation

Create a business website for custom flexible packaging and MDF products. The www.Olvane.com website is generic page that you can use to create a similar home page for my business.
Specifically: https://www.olvane.com/packaging/
https://www.olvane.com/product/mdf-panels/
Domain is Brix-El.com
I would like the page to have a more packaging related look than the MDF/wood.

```html
<!DOCTYPE html>
<html lang="en">
<head>
<meta charset="utf-8">
<title>Brixel Solutions – Flexible Packaging &amp; MDF Products</title>
<link rel="stylesheet" href="https://fonts.googleapis.com/css2?family=Lexend:wght@400;600;700&family=Poppins:wght@400;500;600&display=swap">
<style>
:root{
  --navy:#1b2a4e;
  --navy-dark:#16223f;
  --blue:#1e9bf0;
  --blue-deep:#0b7fd6;
  --ink:#2b2f3a;
  --muted:#5d6577;
  --pale:#eef1f8;
  --line:#d8deea;
  --white:#ffffff;
}
*{box-sizing:border-box;margin:0;padding:0}
html,body{width:1200px;height:4669px;overflow:hidden}
body{position:relative;background:var(--white);font-family:"Poppins",sans-serif;color:var(--ink);font-size:13px}
.abs{position:absolute}
a{color:inherit;text-decoration:none}

/* header */
.site-header{position:absolute;left:0;top:0;width:1200px;height:92px;background:var(--white)}
.brand{position:absolute;display:flex;align-items:center;gap:8px;font-family:"Lexend",sans-serif;font-weight:600;font-size:20px;color:var(--navy);white-space:nowrap}
.brand-dot{width:40px;height:40px;border-radius:50%;background:var(--blue);flex:none}
.search{position:absolute;left:363px;top:25px;width:525px;height:40px;border:1px solid var(--line);border-radius:20px;display:flex;align-items:center;font-size:11px;color:var(--muted)}
.search .cat{width:155px;padding-left:28px;border-right:1px solid var(--line);height:100%;display:flex;align-items:center;justify-content:space-between;padding-right:16px;color:var(--ink)}
.search .field{padding-left:18px;flex:1;color:#9aa1b0}
.search .go{width:30px;height:30px;border-radius:50%;background:var(--blue);margin-right:6px;display:flex;align-items:center;justify-content:center}
.hicon{position:absolute;top:27px;width:38px;height:38px;border-radius:50%;border:1px solid var(--line);display:flex;align-items:center;justify-content:center}
.badge{position:absolute;top:-4px;right:-2px;width:14px;height:14px;border-radius:50%;background:#e53935;color:#fff;font-size:8px;display:flex;align-items:center;justify-content:center}

.main-nav{position:absolute;left:0;top:92px;width:1200px;height:44px;background:var(--navy);font-size:12px;font-weight:500;color:var(--white)}
.main-nav .home{position:absolute;left:0;top:0;width:218px;height:44px;background:linear-gradient(90deg,var(--navy),var(--blue-deep))}
.main-nav span{position:absolute;top:0;line-height:44px;transform:translateX(-50%)}

/* hero */
.hero{position:absolute;left:0;top:136px;width:1200px;height:589px;overflow:hidden;background:linear-gradient(180deg,#f3f5f9,#e7ebf2);border-bottom-left-radius:55% 80px;border-bottom-right-radius:45% 170px}
.hero-photo{position:absolute;left:440px;top:0;width:760px;height:589px;background:radial-gradient(ellipse at 60% 55%,#8a6a4c 0,#b9a48a 18%,#d8dde5 45%,#c2c8d2 70%,#aab2be 100%)}
.hero-photo::before{content:"";position:absolute;inset:0;background:linear-gradient(90deg,#eef1f6 0,rgba(238,241,246,0) 35%)}
.hero h1{position:absolute;left:141px;top:102px;font-family:"Lexend",sans-serif;font-weight:700;font-size:47px;line-height:54px;color:var(--navy)}
.hero h1 em{font-style:normal;font-weight:400;color:var(--blue)}
.hero .tag{position:absolute;left:141px;top:218px;font-size:18px;letter-spacing:8px;color:var(--navy);font-weight:500}
.hero p{position:absolute;left:141px;top:264px;width:460px;font-size:12px;line-height:22px;color:var(--ink)}
.btn{position:absolute;display:flex;align-items:center;justify-content:space-between;border-radius:22px;font-size:11.5px;font-weight:500;text-transform:uppercase}
.btn .arr{width:30px;height:30px;border-radius:50%;background:var(--navy);display:flex;align-items:center;justify-content:center}
.btn-blue{background:var(--blue);color:#fff;padding:0 5px 0 14px}

/* section titles */
.sec-title{position:absolute;left:0;width:1200px;text-align:center;font-family:"Lexend",sans-serif;font-size:36px;font-weight:700;color:var(--navy)}
.sec-title em{font-style:normal;font-weight:400;color:var(--blue)}
.rule{position:absolute;width:70px;height:4px;background:linear-gradient(90deg,var(--navy) 0 55%,transparent 55% 62%,var(--blue) 62%)}
.sec-lead{position:absolute;left:0;width:1200px;text-align:center;font-size:13px;line-height:23px;color:var(--ink)}
.eyebrow{position:absolute;left:0;width:1200px;text-align:center;font-size:14px;letter-spacing:7px;color:var(--navy)}

/* product cards */
.card{position:absolute;width:285px;height:347px;border-radius:14px;overflow:hidden}
.card .photo{position:absolute;inset:0}
.card .body{position:absolute;left:14px;right:14px;bottom:12px;height:104px;background:#fff;border-radius:10px;padding:18px 26px 0}
.card h3{font-size:13px;font-weight:600;color:var(--navy);margin-bottom:8px}
.card p{font-size:12.5px;line-height:20px;color:var(--ink)}
.card.active{box-shadow:0 0 0 3px var(--blue-deep) inset}
.arrow{position:absolute;width:34px;height:34px;border-radius:50%;background:#fff;box-shadow:0 2px 8px rgba(27,42,78,.2);display:flex;align-items:center;justify-content:center;z-index:3}
.rail{position:absolute;left:56px;top:988px;width:14px;height:834px;background:#f1f3f8;border-radius:3px}
.rail::before{content:"";position:absolute;left:5px;top:30px;width:4px;height:90px;background:#dde2ec;border-radius:2px}

/* about */
.about{position:absolute;left:0;top:1969px;width:1200px;height:572px;background:var(--pale)}
.about-arc{position:absolute;left:141px;top:50px}
.about-photo{position:absolute;left:141px;top:55px;width:390px;height:390px;border-radius:50%;background:radial-gradient(circle at 55% 65%,#a07a52 0,#6f5a45 25%,#2e3a55 55%,#1c2740 100%)}
.about .eb{position:absolute;left:631px;top:68px;font-size:14px;letter-spacing:7px;color:var(--navy)}
.about h2{position:absolute;left:631px;top:92px;font-family:"Lexend",sans-serif;font-weight:700;font-size:34px;line-height:38px;color:var(--navy)}
.about h2 em{font-style:normal;font-weight:400;color:var(--blue)}
.about p{position:absolute;left:631px;top:207px;width:420px;font-size:12.5px;line-height:24px}

/* why choose */
.feature{position:absolute;width:90px;height:90px;margin:-45px 0 0 -45px;border-radius:50%;background:#fff;border:2px solid #cfe7fa;box-shadow:0 4px 12px rgba(30,155,240,.12);display:flex;align-items:center;justify-content:center}
.flabel{position:absolute;font-size:14px;font-weight:600;line-height:19px;color:var(--navy);text-transform:uppercase}
.flabel.r{text-align:right}
.core{position:absolute;left:401px;top:2832px;width:398px;height:398px;border-radius:50%;background:var(--navy);display:flex;align-items:center;justify-content:center;color:#fff;font-family:"Lexend",sans-serif;font-size:46px;font-weight:600}

/* industries */
.industries{position:absolute;left:0;top:3459px;width:1200px;height:553px;background:var(--pale)}
.ind{position:absolute;top:197px;width:215px;height:269px;border-radius:10px;overflow:hidden;color:#fff;font-size:13px;font-weight:600;text-align:center;text-transform:uppercase;line-height:18px}
.ind .photo{position:absolute;inset:0}
.ind .photo::after{content:"";position:absolute;inset:0;background:linear-gradient(180deg,rgba(27,42,78,0) 40%,rgba(27,42,78,.9))}
.ind span{position:absolute;left:0;right:0;bottom:28px;z-index:2}

/* cta */
.cta{position:absolute;left:0;top:4012px;width:1200px;height:217px;background:linear-gradient(90deg,var(--blue-deep),var(--blue))}
.cta h2{position:absolute;left:141px;top:80px;font-family:"Lexend",sans-serif;font-weight:700;font-size:34px;color:#fff}
.cta p{position:absolute;left:141px;top:131px;font-size:12.5px;color:#fff}
.btn-white{background:#fff;color:var(--navy);padding:0 5px 0 14px}

/* footer */
.footer{position:absolute;left:0;top:4229px;width:1200px;height:440px;background:var(--navy);color:#d6dcea}
.footer .news{position:absolute;left:861px;top:0;width:339px;height:375px;background:var(--navy-dark);border-left:2px solid var(--blue-deep)}
.footer h4{position:absolute;font-size:14px;font-weight:600;color:#fff}
.footer h4::after{content:"";position:absolute;left:0;bottom:-8px;width:28px;height:3px;background:var(--blue)}
.footer .links{position:absolute;left:419px;top:151px;font-size:12px;line-height:29px}
.citem{position:absolute;left:618px;display:flex;gap:16px;font-size:12px;line-height:18px}
.citem i{width:26px;height:26px;border-radius:50%;background:#2c3b63;display:flex;align-items:center;justify-content:center;flex:none}
.social{position:absolute;top:4500px;width:14px;height:14px;border-radius:50%;border:2px solid #fff}
.input{position:absolute;left:919px;top:4431px;width:198px;height:38px;border:1px solid #4a5880;border-radius:19px;font-size:11px;color:#9aa6c2;padding-left:22px;line-height:36px}
.subscribe{position:absolute;left:919px;top:4485px;width:198px;height:38px;border-radius:19px;background:var(--blue);color:#fff;font-size:12px;font-weight:500;text-align:center;line-height:38px}
.bottom-bar{position:absolute;left:0;top:4604px;width:1200px;height:65px;border-top:1px solid #2f3e66;background:var(--navy);font-size:11px;color:#c9d1e3}
</style>
</head>
<body>

<header class="site-header">
  <div class="brand" style="left:141px;top:25px"><span class="brand-dot"></span>Brixel Solutions</div>
  <div class="search">
    <div class="cat">All Category
      <svg width="10" height="10" viewBox="0 0 10 10"><path d="M2 3l3 3 3-3" fill="none" stroke="#2b2f3a" stroke-width="1.4"/></svg></div>
    <div class="field">Search Products...</div>
    <div class="go"><svg width="14" height="14" viewBox="0 0 14 14"><circle cx="6" cy="6" r="4" fill="none" stroke="#fff" stroke-width="1.8"/><path d="M9 9l3 3" stroke="#fff" stroke-width="1.8"/></svg></div>
  </div>
  <div class="hicon" style="left:924px"><svg width="18" height="16" viewBox="0 0 18 16"><path d="M9 15S1 10 1 5a4 4 0 0 1 8-1 4 4 0 0 1 8 1c0 5-8 10-8 10z" fill="#1e9bf0"/></svg></div>
  <div class="hicon" style="left:973px"><svg width="18" height="16" viewBox="0 0 18 16"><path d="M1 1h3l2 9h9l2-6H5" fill="none" stroke="#1e9bf0" stroke-width="2"/><circle cx="7" cy="14" r="1.5" fill="#1e9bf0"/><circle cx="14" cy="14" r="1.5" fill="#1e9bf0"/></svg><span class="badge">0</span></div>
  <div class="hicon" style="left:1020px"><svg width="16" height="16" viewBox="0 0 16 16"><circle cx="8" cy="5" r="3.5" fill="#1e9bf0"/><path d="M1 16a7 6 0 0 1 14 0z" fill="#1e9bf0"/></svg></div>
</header>

<nav class="main-nav">
  <div class="home"></div>
  <span style="left:160px">HOME</span>
  <span style="left:308px">PRODUCTS</span>
  <span style="left:475px">INDUSTRIES</span>
  <span style="left:638px">ABOUT US</span>
  <span style="left:807px">CONTACT US</span>
  <span style="left:1001px">REQUEST A QUOTE</span>
</nav>

<section class="hero">
  <div class="hero-photo" role="img" aria-label="Flexible packaging pouches, film roll and boxes on a white table in a production plant"></div>
  <h1>Flexible Packaging<br>&amp; <em>MDF Products</em></h1>
  <div class="tag">BUILT FOR YOUR BUSINESS</div>
  <p>Innovative packaging solutions and high quality MDF panels tailored to your exact specifications. From concept to delivery.</p>
  <a class="btn btn-blue" style="left:141px;top:340px;width:178px;height:42px">Request a Quote<span class="arr"><svg width="12" height="12" viewBox="0 0 12 12"><path d="M2 10L10 2M4 2h6v6" fill="none" stroke="#fff" stroke-width="1.6"/></svg></span></a>
</section>

<div class="rail"></div>

<!-- Flexible packaging -->
<h2 class="sec-title" style="top:798px">Flexible Packaging <em>Built for Every Industry</em></h2>
<div class="rule" style="left:565px;top:854px"></div>
<p class="sec-lead" style="top:874px">Stand-up pouches, vacuum pouches, roll stock films, shrink films, and custom packaging<br>designed for performance and durability.</p>

<div class="arrow" style="left:124px;top:1100px"><svg width="10" height="10" viewBox="0 0 10 10"><path d="M6.5 1.5L3 5l3.5 3.5" fill="none" stroke="#1b2a4e" stroke-width="1.6"/></svg></div>
<div class="card" style="left:141px;top:955px"><div class="photo" role="img" aria-label="Vacuum pouches filled with berries and coffee beans" style="background:linear-gradient(160deg,#e8e6e2,#8b5a3c 55%,#4a2a22)"></div><div class="body"><h3>VACUUM POUCHES</h3><p>Lorem Ipsum is simply dummy text of the printing.</p></div></div>
<div class="card" style="left:457px;top:955px"><div class="photo" role="img" aria-label="Clear plastic and glass bottles on a shelf" style="background:linear-gradient(170deg,#f2f2f0,#c9c6c0 55%,#6d5a48)"></div><div class="body"><h3>PLASTIC &amp; GLASS BOTTLES</h3><p>Lorem Ipsum is simply dummy text of the printing.</p></div></div>
<div class="card" style="left:774px;top:955px"><div class="photo" role="img" aria-label="Roll stock film cores in a warehouse" style="background:linear-gradient(180deg,#5d626b,#aeb2b8 50%,#d6d8dc)"></div><div class="body"><h3>ROLL STOCK FILMS</h3><p>Lorem Ipsum is simply dummy text of the printing.</p></div></div>
<div class="arrow" style="left:1042px;top:1100px"><svg width="10" height="10" viewBox="0 0 10 10"><path d="M3.5 1.5L7 5 3.5 8.5" fill="none" stroke="#1b2a4e" stroke-width="1.6"/></svg></div>

<!-- Safety -->
<h2 class="sec-title" style="top:1378px">Safety Supplies <em>That Protects Your Workforce</em></h2>
<div class="rule" style="left:565px;top:1433px"></div>
<p class="sec-lead" style="top:1453px">Hand protection, protective garments, masks, eye protection, head protection, and sleeves for<br>complete workplace safety.</p>

<div class="arrow" style="left:124px;top:1680px"><svg width="10" height="10" viewBox="0 0 10 10"><path d="M6.5 1.5L3 5l3.5 3.5" fill="none" stroke="#1b2a4e" stroke-width="1.6"/></svg></div>
<div class="card" style="left:141px;top:1535px"><div class="photo" role="img" aria-label="White work gloves with dotted grip" style="background:linear-gradient(160deg,#e4e6ea,#b8bcc4 60%,#8b919c)"></div><div class="body"><h3>HAND PROTECTION</h3><p>Lorem Ipsum is simply dummy text of the printing.</p></div></div>
<div class="card active" style="left:457px;top:1535px"><div class="photo" role="img" aria-label="Clear safety glasses on a blue background" style="background:linear-gradient(170deg,#cfd8e2,#8fa9c4 55%,#3e6fa8)"></div><div class="body"><h3>EYE PROTECTION</h3><p>Lorem Ipsum is simply dummy text of the printing.</p></div></div>
<div class="card" style="left:774px;top:1535px"><div class="photo" role="img" aria-label="White hard hat on a wooden surface" style="background:linear-gradient(150deg,#f3f3f3,#d9d9d9 45%,#9b7352 80%)"></div><div class="body"><h3>HEAD PROTECTION</h3><p>Lorem Ipsum is simply dummy text of the printing.</p></div></div>
<div class="arrow" style="left:1042px;top:1680px"><svg width="10" height="10" viewBox="0 0 10 10"><path d="M3.5 1.5L7 5 3.5 8.5" fill="none" stroke="#1b2a4e" stroke-width="1.6"/></svg></div>

<!-- About -->
<section class="about">
  <svg class="about-arc" width="440" height="410" viewBox="0 0 440 410"><path d="M25 150 A205 205 0 0 1 430 205" fill="none" stroke="#1e9bf0" stroke-width="30"/></svg>
  <div class="about-photo" role="img" aria-label="Kraft and printed stand-up pouches in front of packaging machinery"></div>
  <div class="eb">ABOUT US</div>
  <h2>Manufacturing<br>Excellence <em>Since Day One</em></h2>
  <div class="rule" style="left:631px;top:179px"></div>
  <p>Brixel Industries is a leading manufacturer of flexible packaging materials and MDF products. With state-of-the-art machinery, stringent quality controls, and a dedicated team, we deliver packaging solutions that protect your products and enhance your brand. FlexWeave MDF combines decades of experience in flexible packaging manufacturing with precision MDF engineering. We help brands and manufacturers reduce costs, improve sustainability, and stand out on the shelf.</p>
  <a class="btn btn-blue" style="left:631px;top:427px;width:136px;height:40px">Read More<span class="arr"><svg width="12" height="12" viewBox="0 0 12 12"><path d="M2 10L10 2M4 2h6v6" fill="none" stroke="#fff" stroke-width="1.6"/></svg></span></a>
</section>

<!-- Why choose -->
<div class="eyebrow" style="top:2622px">WHY CHOOSE US</div>
<h2 class="sec-title" style="top:2638px">Why Choose Us <em>As Your Packaging Partner</em></h2>
<div class="rule" style="left:565px;top:2693px"></div>
<p class="sec-lead" style="top:2714px">We combine quality, reliability, and global sourcing expertise to deliver packaging solutions that<br>meet your exact business needs.</p>

<svg class="abs" style="left:335px;top:2766px" width="530" height="530" viewBox="0 0 530 530"><circle cx="265" cy="265" r="263" fill="none" stroke="#8a8f9c" stroke-width="1.4" stroke-dasharray="5 5"/></svg>
<div class="core">Brixel</div>

<div class="feature" style="left:419px;top:2833px"><svg width="46" height="46" viewBox="0 0 46 46" fill="none" stroke="#1b2a4e" stroke-width="2"><circle cx="24" cy="15" r="7"/><circle cx="24" cy="15" r="2.5" stroke="#1e9bf0"/><path d="M4 32h8l8 3h10l10-6M12 32v10H4"/></svg></div>
<div class="feature" style="left:785px;top:2833px"><svg width="46" height="46" viewBox="0 0 46 46" fill="none" stroke="#1b2a4e" stroke-width="2"><circle cx="23" cy="12" r="5"/><circle cx="11" cy="16" r="4"/><circle cx="35" cy="16" r="4"/><path d="M14 34a9 9 0 0 1 18 0M4 32a7 7 0 0 1 12-4M42 32a7 7 0 0 0-12-4"/><path d="M8 38h30" stroke="#1e9bf0"/></svg></div>
<div class="feature" style="left:337px;top:3024px"><svg width="46" height="46" viewBox="0 0 46 46" fill="none" stroke="#1b2a4e" stroke-width="2"><circle cx="26" cy="25" r="13"/><path d="M26 17v8l5 4M23 8h6M4 20h8M2 26h8M4 32h8" /><path d="M26 12v-4" stroke="#1e9bf0"/></svg></div>
<div class="feature" style="left:866px;top:3024px"><svg width="46" height="46" viewBox="0 0 46 46" fill="none" stroke="#1b2a4e" stroke-width="2"><circle cx="23" cy="23" r="15"/><path d="M23 15l2.5 5 5.5.8-4 3.8 1 5.4-5-2.6-5 2.6 1-5.4-4-3.8 5.5-.8z" stroke="#1e9bf0"/></svg></div>
<div class="feature" style="left:419px;top:3212px"><svg width="46" height="46" viewBox="0 0 46 46" fill="none" stroke="#1b2a4e" stroke-width="2"><circle cx="23" cy="23" r="16"/><path d="M7 23h32M23 7c6 5 6 27 0 32M23 7c-6 5-6 27 0 32"/><path d="M30 30l8 8" stroke="#1e9bf0"/></svg></div>
<div class="feature" style="left:785px;top:3212px"><svg width="46" height="46" viewBox="0 0 46 46" fill="none" stroke="#1b2a4e" stroke-width="2"><path d="M23 5l5 4 6 0 1 6 5 4-3 6 1 6-6 2-3 5-6-2-6 2-3-5-6-2 1-6-3-6 5-4 1-6 6 0z"/><path d="M16 22l5 5 10-10" stroke="#1e9bf0"/></svg></div>
<div class="feature" style="left:600px;top:3296px"><svg width="46" height="46" viewBox="0 0 46 46" fill="none" stroke="#1b2a4e" stroke-width="2"><circle cx="23" cy="23" r="9"/><path d="M23 6v6M23 34v6M6 23h6M34 23h6M11 11l4 4M31 31l4 4M35 11l-4 4M11 35l4-4"/><path d="M20 26c0-5 3-7 7-8 0 4-2 7-7 8z" stroke="#1e9bf0"/></svg></div>

<div class="flabel r" style="right:856px;top:2813px">Custom<br>Manufacturing</div>
<div class="flabel" style="left:866px;top:2813px">Expert<br>Support</div>
<div class="flabel r" style="right:937px;top:3008px">Fast<br>Production</div>
<div class="flabel" style="left:937px;top:3008px">15+ Years<br>Experience</div>
<div class="flabel r" style="right:865px;top:3222px">Worldwide<br>Shipping</div>
<div class="flabel" style="left:859px;top:3222px">Quality<br>Assurance</div>
<div class="flabel" style="left:0;width:1200px;text-align:center;top:3357px">Sustainable Materials</div>

<!-- Industries -->
<section class="industries">
  <div class="eyebrow" style="top:80px">INDUSTRIES</div>
  <h2 class="sec-title" style="top:96px">Industries Served <em>With Quality &amp; Trust</em></h2>
  <div class="rule" style="left:565px;top:150px"></div>
  <div class="arrow" style="left:124px;top:314px"><svg width="10" height="10" viewBox="0 0 10 10"><path d="M6.5 1.5L3 5l3.5 3.5" fill="none" stroke="#1b2a4e" stroke-width="1.6"/></svg></div>
  <div class="ind" style="left:143px"><div class="photo" role="img" aria-label="Hand holding a packaged food box" style="background:linear-gradient(160deg,#e9e4dc,#c8a46a 45%,#6b5a4a)"></div><span>Food &amp; Beverage</span></div>
  <div class="ind" style="left:377px"><div class="photo" role="img" aria-label="Bottles moving along an industrial filling line" style="background:linear-gradient(170deg,#d7dbe0,#a9a48a 50%,#b88a2e)"></div><span>Industrial<br>Manufacturing</span></div>
  <div class="ind" style="left:611px"><div class="photo" role="img" aria-label="Pharmaceutical bottles held in a gloved hand" style="background:linear-gradient(170deg,#6a4e40,#c7cdd3 45%,#7fa894)"></div><span>Pharmaceuticals<br>&amp; Healthcare</span></div>
  <div class="ind" style="left:843px"><div class="photo" role="img" aria-label="Hands holding soil with a green seedling" style="background:radial-gradient(circle at 50% 40%,#5fa83a 0,#4a3a2c 35%,#8a8f96 80%)"></div><span>Agriculture</span></div>
  <div class="arrow" style="left:1042px;top:314px"><svg width="10" height="10" viewBox="0 0 10 10"><path d="M3.5 1.5L7 5 3.5 8.5" fill="none" stroke="#1b2a4e" stroke-width="1.6"/></svg></div>
</section>

<!-- CTA -->
<section class="cta">
  <h2>Let’s Build Your Packaging Solution</h2>
  <p>Speak directly with our packaging expert team and get customized solutions for your business needs.</p>
  <a class="btn btn-white" style="left:915px;top:90px;width:146px;height:44px">Contact Us<span class="arr"><svg width="12" height="12" viewBox="0 0 12 12"><path d="M2 10L10 2M4 2h6v6" fill="none" stroke="#fff" stroke-width="1.6"/></svg></span></a>
</section>

<!-- Footer -->
<footer class="footer">
  <div class="news"></div>
  <div class="brand" style="left:82px;top:102px;color:#fff"><span class="brand-dot"></span>Brixel Solutions</div>
  <p class="abs" style="left:82px;top:192px;width:290px;font-size:11.5px;line-height:18px">Your trusted global source for innovative packaging solutions, committed to quality, consistency, and long-term partnerships.</p>
  <h4 style="left:419px;top:102px">Quick Links</h4>
  <div class="links"><div>Home</div><div>Products</div><div>Industries</div><div>About Us</div><div>Contact Us</div></div>
  <h4 style="left:618px;top:102px">Contact Us</h4>
  <h4 style="left:919px;top:101px">Subscribe to Newsletter</h4>
  <p class="abs" style="left:919px;top:140px;width:220px;font-size:11px;line-height:18px">Join thousands of readers getting our best content every week.</p>
</footer>
<div class="citem" style="top:4379px"><i><svg width="12" height="10" viewBox="0 0 12 10"><rect x="1" y="1" width="10" height="8" fill="none" stroke="#fff" stroke-width="1.2"/><path d="M1 1l5 4 5-4" fill="none" stroke="#fff" stroke-width="1.2"/></svg></i><span style="line-height:26px;color:#d6dcea">Dana@Brix-El.com</span></div>
<div class="citem" style="top:4424px"><i><svg width="12" height="12" viewBox="0 0 12 12"><path d="M2 1h3l1 3-2 1a7 7 0 0 0 3 3l1-2 3 1v3c-6 0-9-3-9-9z" fill="#fff"/></svg></i><span style="line-height:26px;color:#d6dcea">(555)-214-7730</span></div>
<div class="citem" style="top:4470px"><i><svg width="10" height="13" viewBox="0 0 10 13"><path d="M5 12S1 7 1 4.5a4 4 0 0 1 8 0C9 7 5 12 5 12z" fill="#fff"/><circle cx="5" cy="4.5" r="1.5" fill="#2c3b63"/></svg></i><span style="color:#d6dcea">482 Mill Creek Rd.<br>Fairview, AR 72000</span></div>
<span class="social" style="left:82px"></span>
<span class="social" style="left:118px"></span>
<span class="social" style="left:157px"></span>
<span class="social" style="left:195px"></span>
<div class="input">Enter your email</div>
<div class="subscribe">SUBSCRIBE NOW</div>
<div class="bottom-bar">
  <span class="abs" style="left:82px;top:26px">Copyright © 2026 Brixel MDF Products | All Rights Reserved.</span>
  <span class="abs" style="right:90px;top:26px">Privacy Policy &nbsp;|&nbsp; Terms &amp; Conditions</span>
</div>

</body>
</html>
```